Valbrook Data Works

Our company is about IT hardwares and IT solutions. IT hardware such as PC, RAMS, storage and servers. IT solutions such as project management, BA. We are also selling new technology too.

Target Market(s)

Consumer, Small to Medium Business, Corporate

Requirements
Must have
• The business card must have the following:
• Name:
• Title:
• Contact Number:
• Email address:
• Website:
• Color: Must match the logo color upgrade

```html
<!DOCTYPE html>
<html lang="en">
<head>
<meta charset="utf-8">
<title>Valbrook Data Works – Business Card</title>
<link rel="stylesheet" href="https://fonts.googleapis.com/css2?family=Arimo:wght@400;700&family=Rubik:wght@700&display=swap">
<style>
  :root {
    --page-bg: #e8e4de;
    --panel-dark: #2c2c2e;
    --panel-mid: #46464a;
    --frost-light: #eeeeee;
    --frost-mid: #d6d4d2;
    --accent: #b5541f;
    --text-light: #e6e2dc;
    --text-soft: #cfcac4;
    --brand-ink: #1c1c1e;
  }
  html, body {
    margin: 0;
    width: 1200px;
    height: 970px;
    overflow: hidden;
    background: var(--page-bg);
  }
  .business-card {
    position: absolute;
    left: 184px;
    top: 249px;
    width: 832px;
    height: 472px;
    border-radius: 24px;
    overflow: hidden;
    box-shadow: 0 12px 32px rgba(0,0,0,0.18);
    font-family: "Arimo", Arial, sans-serif;
  }
  .card-shapes {
    position: absolute;
    inset: 0;
  }
  .contact-side {
    position: absolute;
    left: 50px;
    top: 0;
    color: var(--text-soft);
  }
  .person-name {
    position: absolute;
    top: 86px;
    margin: 0;
    font-size: 24px;
    font-weight: 700;
    color: var(--text-light);
    white-space: nowrap;
    letter-spacing: 0.3px;
  }
  .person-title {
    position: absolute;
    top: 110px;
    margin: 0;
    font-size: 20px;
    color: var(--text-light);
  }
  .postal-address {
    position: absolute;
    top: 244px;
    margin: 0;
    font-size: 20px;
    font-style: normal;
    line-height: 26px;
    white-space: nowrap;
  }
  .contact-list {
    position: absolute;
    top: 314px;
    margin: 0;
    padding: 0;
    list-style: none;
    font-size: 20px;
    line-height: 26px;
    white-space: nowrap;
  }
  .contact-list li {
    display: flex;
    align-items: center;
    gap: 12px;
  }
  .contact-icon {
    width: 18px;
    height: 18px;
    flex: none;
  }
  .brand-block {
    position: absolute;
    left: 450px;
    right: 0;
    top: 150px;
    text-align: center;
  }
  .brand-dot {
    display: block;
    width: 40px;
    height: 40px;
    margin: 0 auto 18px;
    border-radius: 50%;
    background: var(--accent);
  }
  .brand-name {
    margin: 0;
    font-family: "Rubik", Arial, sans-serif;
    font-weight: 700;
    font-size: 36px;
    line-height: 42px;
    color: var(--brand-ink);
    text-transform: uppercase;
  }
</style>
</head>
<body>
  <div class="business-card">
    <svg class="card-shapes" width="832" height="472" viewBox="0 0 832 472" aria-hidden="true">
      <defs>
        <linearGradient id="frost" x1="0" y1="0" x2="1" y2="1">
          <stop offset="0" stop-color="var(--frost-light)"/>
          <stop offset="1" stop-color="var(--frost-mid)"/>
        </linearGradient>
        <linearGradient id="dark" x1="0" y1="0" x2="1" y2="1">
          <stop offset="0" stop-color="var(--panel-dark)"/>
          <stop offset="0.55" stop-color="var(--panel-mid)"/>
          <stop offset="1" stop-color="var(--panel-dark)"/>
        </linearGradient>
      </defs>
      <rect class="frost-side" width="832" height="472" fill="url(#frost)"/>
      <path class="dark-panel" d="M0 0 H435 Q325 236 435 472 H0 Z" fill="url(#dark)"/>
      <path class="accent-curve" d="M444 0 Q334 236 444 472" fill="none" stroke="var(--accent)" stroke-width="3"/>
      <circle class="edge-notch" cx="0" cy="104" r="24" fill="var(--page-bg)"/>
    </svg>

    <div class="contact-side">
      <h1 class="person-name">MARA ELLISON</h1>
      <p class="person-title">Manager</p>
      <address class="postal-address">PO BOX 418 Harlow Lane<br>4th street Kestwood</address>
      <ul class="contact-list">
        <li>
          <svg class="contact-icon" viewBox="0 0 18 18"><path d="M2 8 Q9 1 16 8 L14 10 L12 8 L6 8 L4 10 Z M5 10 H13 L14 15 H4 Z" fill="var(--text-soft)"/></svg>
          555-204-7316
        </li>
        <li>
          <svg class="contact-icon" viewBox="0 0 18 18"><rect x="2" y="4" width="14" height="10" fill="none" stroke="var(--text-soft)" stroke-width="1.5"/><path d="M2 4 L9 10 L16 4 M2 14 L7 9 M16 14 L11 9" fill="none" stroke="var(--text-soft)" stroke-width="1.3"/></svg>
          info@valbrookdata.com
        </li>
        <li>
          <svg class="contact-icon" viewBox="0 0 18 18"><circle cx="9" cy="9" r="7" fill="none" stroke="var(--text-soft)" stroke-width="1.3"/><ellipse cx="9" cy="9" rx="3" ry="7" fill="none" stroke="var(--text-soft)" stroke-width="1.1"/><path d="M2 9 H16 M3.5 5.5 H14.5 M3.5 12.5 H14.5" stroke="var(--text-soft)" stroke-width="1"/></svg>
          www.valbrookdata.com
        </li>
      </ul>
    </div>

    <div class="brand-block">
      <span class="brand-dot"></span>
      <p class="brand-name">Valbrook<br>Data Works</p>
    </div>
  </div>
</body>
</html>
```